Townhome Multi-Family Property Exterior Sign

Hello. We are looking for a new design for our exterior pylon for for a multi-family housing property in Texas. The design will need to go on a new sign panel to replace the existing (see photo of existing). We are looking to see both modern and contemporary designs. Included the sign should be the name, Loma Brisa Townhomes and the web address www.lomabrisatownhomes.example.

Attached here is a PDF file of the proposed new sign shape. We are open to other shape ideas as well if your design would better suit a more rectangular shape.

Industry/Entity Type

Property

Font styles to use
Serif
Sans Serif

Colors
9bcb3c

Requirements
Must have
• Name of building: Loma Brisa Townhomes
• Website: www.lomabrisatownhomes.example
Nice to have
• Address: 412-590 Halvern Ridge Drive (only if it fits nicely)

```html
<!DOCTYPE html>
<html lang="en">
<head>
<meta charset="utf-8">
<title>Loma Brisa Townhomes – Exterior Sign Panel</title>
<link rel="stylesheet" href="https://fonts.googleapis.com/css2?family=Jost:wght@500;600&display=swap">
<style>
  :root {
    --sign-green: #4c974a;
    --sign-white: #ffffff;
    --page-bg: #ffffff;
  }
  html, body {
    margin: 0;
    padding: 0;
    width: 1200px;
    height: 683px;
    overflow: hidden;
    background: var(--page-bg);
  }
  .sign {
    position: relative;
    width: 1200px;
    height: 683px;
  }
  .sign-shape {
    position: absolute;
    inset: 0;
    display: block;
  }
  .sign-shape path { fill: var(--sign-green); }
  .sign-name,
  .sign-subtitle,
  .sign-web {
    position: absolute;
    left: 0;
    width: 1200px;
    margin: 0;
    text-align: center;
    color: var(--sign-white);
    font-family: "Jost", sans-serif;
  }
  .sign-name {
    top: 268px;
    font-size: 118px;
    font-weight: 500;
    line-height: 1;
    letter-spacing: 2px;
  }
  .sign-subtitle {
    top: 428px;
    font-size: 40px;
    font-weight: 600;
    line-height: 1;
    letter-spacing: 30px;
    text-indent: 30px;
  }
  .sign-web {
    top: 529px;
    font-size: 19px;
    font-weight: 600;
    line-height: 1;
    letter-spacing: 0.6px;
  }
</style>
</head>
<body>
  <main class="sign">
    <svg class="sign-shape" width="1200" height="683" viewBox="0 0 1500 853" preserveAspectRatio="none" aria-hidden="true">
      <path d="M0 485
               C8 462 38 440 50 385
               C58 350 56 330 60 305
               C72 255 120 245 155 238
               C168 234 166 228 175 215
               C260 120 380 115 520 80
               C620 55 690 20 735 3
               C745 -1 752 -1 762 4
               C800 25 900 65 980 90
               C1100 130 1230 120 1310 205
               C1325 220 1320 238 1340 242
               C1370 248 1405 255 1432 295
               C1445 315 1432 345 1442 385
               C1462 460 1482 468 1500 492
               L1500 853 L0 853 Z"/>
    </svg>
    <h1 class="sign-name">Loma Brisa</h1>
    <p class="sign-subtitle">TOWNHOMES</p>
    <p class="sign-web">www.lomabrisatownhomes.example</p>
  </main>
</body>
</html>
```